One page technology product flyer

We are a technology firm looking to create a one page very professional looking product overview. We provide supply chain consulting specifically around integrating systems and integrating software between trading partners.

See attached Word document for content (Vexa PLT Flyer)

The attached flyer is an example of one our other product flyers. Just example for look and feel.

Text for flyer:
Mornly.io Integration Services

Turn key integration -> Slogan (can be incorporated in to graphic or design box)

Mornly.io provides a fully managed integration service specifically for Logistics Service Providers and Shippers. This includes everything from designing the integration, to project management, implementation and ongoing maintenance.

Our client often employs full time staff to create and manage integrations with their trading partners. Within their corporate silos, these resources can be inefficient and isolated from industry best practices. These efforts are costs impacting the company’s bottom line and are also friction points if they do not operate effectively.

What we offer:
• Design and implementation of new integrations with external trading partners
• The daily care and maintenance of these integrations including trading partner communication and issue resolution

Our services are end-to-end integrations:
• Design
• Project Management
• Mapping & Implementation
• Cloud Execution
• Monitoring & Anomaly Detection
• Incident Response

Why are we unique?
Our solution solves the full integration problem space from inception through operations support. We provide logistics industry specific design services and offer a turnkey solution that includes full monitoring and error correction in production. We do all this via our modular approach.

For more information please contact us at info@mornly.example
555.301.7792 www.mornly.example
info@mornly.example 812 Alder Rd, Suite 540
Philadelphia, PA 19000

Target Market(s)

B2B: Logistics Technology, Supply Chain technology, Software integration

Industry/Entity Type

Logistics

Font styles to use
Other font styles liked:
• Robotto or Like other brochure files

Colors

Designer to choose colors to be used in the design.

Requirements
Must have
• Our logo and company information. One or more graphic illustrations giving a visual idea of what the product does. Nice professional layout. Have available as PDF, but also high resolution enough to print high quality with printing firm.

```html
<!DOCTYPE html>
<html lang="en">
<head>
<meta charset="utf-8">
<title>Mornly.io – Turn Key Integration Flyer</title>
<link rel="stylesheet" href="https://fonts.googleapis.com/css2?family=Montserrat:ital,wght@0,400;0,600;0,700;0,800;1,400;1,600;1,700;1,800&display=swap">
<style>
  :root {
    --page-bg: #e7ebef;
    --sky: #2aa3d9;
    --blue: #1d8fcf;
    --deep: #1a5f9e;
    --navy: #1d3557;
    --slate: #5b6a86;
    --ink: #2c3e57;
    --paper: #ffffff;
    --muted: #f2f5f8;
  }
  * { box-sizing: border-box; margin: 0; padding: 0; }
  html, body { width: 1200px; height: 1200px; overflow: hidden; }
  body {
    background: var(--page-bg);
    font-family: "Montserrat", sans-serif;
    color: var(--ink);
    position: relative;
  }
  .flyer {
    position: absolute;
    left: 200px; top: 35px;
    width: 800px; height: 1130px;
    background: var(--paper);
    overflow: hidden;
    box-shadow: 0 6px 24px rgba(20, 40, 70, .18);
  }
  .flyer__backdrop { position: absolute; inset: 0; }
  .photo {
    position: absolute;
    border-radius: 50%;
    border: 7px solid var(--paper);
  }
  .photo--hero {
    left: 60px; top: 40px; width: 370px; height: 370px;
    background: radial-gradient(circle at 55% 40%, #8fc6e8 0%, #4d7fa6 45%, #2c3e57 100%);
  }
  .photo--devices {
    left: 440px; top: 180px; width: 175px; height: 175px;
    background: radial-gradient(circle at 50% 55%, #6fb6e0 0%, #2f6f9f 70%, #1d3557 100%);
  }
  .photo--technician {
    left: 615px; top: 160px; width: 165px; height: 165px;
    background: linear-gradient(150deg, #9cc7e3 0%, #3f6f95 60%, #23405f 100%);
  }
  .photo--portrait {
    position: absolute;
    left: 0; top: 470px; width: 300px; height: 490px;
    background: linear-gradient(180deg, #9cc3e6 0%, #b7d3ee 45%, #7a9cc4 100%);
  }
  .slogan {
    position: absolute;
    right: 28px; top: 48px;
    width: 320px;
    color: var(--paper);
    font-weight: 800; font-style: italic;
    font-size: 38px; line-height: 1.05;
    text-transform: uppercase;
    letter-spacing: 1px;
    text-align: right;
  }
  .intro {
    position: absolute;
    left: 320px; top: 472px; width: 455px;
    text-align: right;
    font-style: italic; font-weight: 700;
    font-size: 15.5px; line-height: 1.45;
    color: var(--deep);
  }
  .intro strong { color: var(--navy); font-weight: 700; }
  .section-title {
    font-style: italic; font-weight: 800;
    font-size: 17px; color: var(--blue);
    text-transform: uppercase;
    margin-bottom: 8px;
  }
  .offer { position: absolute; left: 320px; top: 655px; width: 230px; }
  .services { position: absolute; left: 575px; top: 655px; width: 210px; }
  .bullets { list-style: none; }
  .bullets li {
    position: relative;
    padding-left: 16px;
    font-style: italic; font-size: 12px; line-height: 1.35;
    color: var(--ink);
    margin-bottom: 4px;
  }
  .offer .bullets li { margin-bottom: 12px; }
  .bullets li::before {
    content: ""; position: absolute; left: 0; top: 5px;
    width: 7px; height: 7px; border-radius: 50%;
    background: var(--navy);
  }
  .unique { position: absolute; left: 320px; top: 845px; width: 460px; }
  .unique p { font-style: italic; font-size: 12px; line-height: 1.4; }
  .footer {
    position: absolute; left: 0; right: 0; bottom: 0; height: 165px;
    background: var(--muted);
    display: flex; align-items: center;
    padding: 0 26px;
  }
  .brand {
    display: flex; align-items: center; gap: 8px;
    width: 210px; flex-shrink: 0;
    font-weight: 800; font-style: italic;
    font-size: 36px; color: var(--blue);
  }
  .brand__dot { width: 13px; height: 13px; border-radius: 50%; background: var(--blue); }
  .footer__divider { width: 2px; height: 100px; background: var(--navy); margin: 0 22px; flex-shrink: 0; }
  .contact { font-style: italic; font-size: 12.5px; line-height: 1.8; color: var(--navy); font-weight: 700; }
  .contact__lead { color: var(--blue); font-size: 13.5px; }
  .contact__row { display: flex; gap: 14px; align-items: center; white-space: nowrap; }
  .contact__item { display: inline-flex; align-items: center; gap: 5px; white-space: nowrap; }
  .contact svg { width: 13px; height: 13px; fill: var(--navy); flex-shrink: 0; }
</style>
</head>
<body>
  <article class="flyer">
    <svg class="flyer__backdrop" viewBox="0 0 800 1130" preserveAspectRatio="none" aria-hidden="true">
      <polygon points="0,0 800,0 800,300 0,480" fill="#2aa3d9"/>
      <polygon points="0,0 260,0 120,120 0,170" fill="#5b6a86"/>
      <polygon points="460,0 800,0 800,36 560,36" fill="#1d8fcf"/>
      <polygon points="0,480 800,300 800,330 0,512" fill="#1d3557"/>
      <polygon points="0,512 800,330 800,342 0,526" fill="#1a5f9e"/>
    </svg>

    <div class="photo photo--hero" role="img" aria-label="Photo: hand holding a laptop with a digital globe and data chart above it"></div>
    <div class="photo photo--devices" role="img" aria-label="Photo: connected laptop, tablet and phone over a world network"></div>
    <div class="photo photo--technician" role="img" aria-label="Photo: technician working in a server room"></div>
    <div class="photo--portrait" role="img" aria-label="Photo: smiling businessman in shirt and tie with arms crossed"></div>

    <h1 class="slogan">Turn Key Integration</h1>

    <p class="intro">Our client often employs full time staff to create and manage integrations with their trading partners. <strong>Within their corporate silos, these resources can be inefficient and isolated from industry best practices.</strong> These efforts are costs impacting the company’s bottom line and are also friction points if they do not operate effectively.</p>

    <section class="offer">
      <h2 class="section-title">What we offer:</h2>
      <ul class="bullets">
        <li>Design and implementation of new integrations with external trading partners.</li>
        <li>The daily care and maintenance of these integrations including trading partner communication and issue resolution.</li>
      </ul>
    </section>

    <section class="services">
      <h2 class="section-title">Our services:</h2>
      <ul class="bullets">
        <li>Design</li>
        <li>Project Management</li>
        <li>Mapping &amp; Implementation</li>
        <li>Cloud Execution</li>
        <li>Monitoring &amp; Anomaly Detection</li>
        <li>Incident Response</li>
      </ul>
    </section>

    <section class="unique">
      <h2 class="section-title">Why are we unique?</h2>
      <p>Our solution solves the full integration problem space from inception through operations support. We provide logistics industry specific design services and offer a turnkey solution that includes full monitoring and error correction in production. We do all this via our modular approach.</p>
    </section>

    <footer class="footer">
      <div class="brand"><span class="brand__dot"></span>Mornly.io</div>
      <div class="footer__divider"></div>
      <div class="contact">
        <div class="contact__lead">For more information please contact us at:</div>
        <div class="contact__row">
          <span class="contact__item"><svg viewBox="0 0 16 16"><path d="M1 3h14v10H1z M1 3l7 6 7-6" fill="none" stroke="#1d3557" stroke-width="1.6"/></svg>info@mornly.example</span>
          <span class="contact__item"><svg viewBox="0 0 16 16"><path d="M3 1l3 0 1 4-2 1.5c1 2 2.5 3.5 4.5 4.5L11 9l4 1v3c0 1-1 2-2 2C6.5 15 1 9.5 1 3c0-1 1-2 2-2z"/></svg>555.301.7792</span>
          <span class="contact__item"><svg viewBox="0 0 16 16"><circle cx="8" cy="8" r="6.5" fill="none" stroke="#1d3557" stroke-width="1.6"/><path d="M1.5 8h13M8 1.5c-3 3.5-3 9.5 0 13M8 1.5c3 3.5 3 9.5 0 13" fill="none" stroke="#1d3557" stroke-width="1.2"/></svg>www.mornly.example</span>
        </div>
        <div class="contact__lead">Or visit our main office at:</div>
        <div class="contact__item"><svg viewBox="0 0 16 16"><path d="M8 1a5 5 0 0 0-5 5c0 4 5 9 5 9s5-5 5-9a5 5 0 0 0-5-5zm0 7a2 2 0 1 1 0-4 2 2 0 0 1 0 4z"/></svg>812 Alder Rd, Suite 540 Philadelphia, PA 19000</div>
      </div>
    </footer>
  </article>
</body>
</html>
```